Letterhead to Prospective Clients

Create a letterhead (word & canva) that I will use to send letters to prospective clients and also include the Coralwood Estate Partners Logo, My Contact Details and Interchangeable "Suburb". Use the same font and colour pallete

Maris Dulworth | "Suburb" Specialist - Redlands & Surrounds
Mobile: 0417 862 095
Email: MD@CoralwoodEstatePartners.com.au

```html
<!DOCTYPE html>
<html lang="en">
<head>
<meta charset="utf-8">
<title>Coralwood Estate Partners – Letterhead</title>
<link rel="stylesheet" href="https://fonts.googleapis.com/css2?family=Roboto:wght@300;400;500;700&display=swap">
<style>
  :root {
    --backdrop: #a3a3a3;
    --navy: #001539;
    --gold: #d4a57c;
    --paper: #f8f9f8;
    --white: #ffffff;
  }
  * { margin: 0; padding: 0; box-sizing: border-box; }
  html, body { width: 1200px; height: 1200px; overflow: hidden; }
  body {
    background: var(--backdrop);
    font-family: "Roboto", Arial, sans-serif;
    color: var(--navy);
    position: relative;
  }
  .wordmark {
    font-family: "Roboto", Arial, sans-serif;
    font-weight: 300;
    text-transform: uppercase;
    text-align: center;
    line-height: 1.15;
  }
  .presentation-brand {
    position: absolute; left: 400px; top: 58px; width: 400px;
    font-size: 30px; letter-spacing: 5px; color: var(--navy);
  }
  .presentation-title {
    position: absolute; left: 0; top: 160px; width: 1200px;
    text-align: center; font-weight: 500; font-size: 24px; letter-spacing: 3.5px;
  }
  .sheet {
    position: absolute; top: 246px; width: 526px; height: 724px; overflow: hidden;
  }
  .sheet--front { left: 57px; background: var(--paper); }
  .sheet--back { left: 628px; background: var(--navy); }
  .band { position: absolute; left: 0; width: 100%; background: var(--navy); }
  .band--top { top: 0; height: 10px; }
  .band--bottom { bottom: 0; height: 11px; }
  .rule { position: absolute; left: 0; width: 100%; height: 2px; background: var(--gold); }
  .rule--top { top: 13px; }
  .rule--bottom { bottom: 16px; }

  .header-brand {
    position: absolute; left: 28px; top: 292px; top: 46px; width: 190px;
    font-size: 20px; letter-spacing: 2.5px; color: var(--navy);
  }
  .header-divider {
    position: absolute; left: 281px; top: 41px; width: 2px; height: 56px; background: var(--gold);
  }
  .header-contact { position: absolute; left: 299px; top: 46px; }
  .contact-name { font-size: 10px; font-weight: 500; line-height: 12px; }
  .contact-role { font-size: 10px; font-weight: 400; line-height: 12px; }
  .contact-line { font-size: 7.5px; font-weight: 500; line-height: 9.5px; }
  .contact-role + .contact-line { margin-top: 5px; }

  .footer-contact {
    position: absolute; left: 30px; top: 676px; font-size: 7.5px; line-height: 12px; font-weight: 500;
  }
  .footer-contact .role { font-weight: 400; margin-left: 3px; }
  .footer-contact .sep { margin: 0 9px; font-weight: 400; }
  .footer-brand {
    position: absolute; left: 390px; top: 666px; width: 112px;
    font-size: 9px; letter-spacing: 1.2px; color: var(--navy);
  }

  .cover-brand {
    position: absolute; left: 63px; top: 280px; width: 400px;
    font-size: 36px; letter-spacing: 5px; color: var(--white); line-height: 1.3;
  }

  .sheet-label {
    position: absolute; top: 986px; width: 300px; text-align: center;
    font-size: 37px; font-weight: 500;
  }
  .sheet-label--front { left: 168px; }
  .sheet-label--back { left: 775px; top: 992px; }
</style>
</head>
<body>
  <div class="presentation-brand wordmark">Coralwood Estate Partners</div>
  <h1 class="presentation-title">LETTERHEAD DESIGN</h1>

  <section class="sheet sheet--front">
    <div class="band band--top"></div>
    <div class="rule rule--top"></div>

    <div class="header-brand wordmark">Coralwood Estate Partners</div>
    <div class="header-divider"></div>
    <div class="header-contact">
      <p class="contact-name">Maris Dulworth</p>
      <p class="contact-role">"Suburb" Specialist - Redlands &amp; Surrounds</p>
      <p class="contact-line">Mobile: 0417 862 095</p>
      <p class="contact-line">Email: MD@CoralwoodEstatePartners.com.au</p>
    </div>

    <div class="footer-contact">
      <p>Maris Dulworth<span class="role">"Suburb" Specialist - Redlands &amp; Surrounds</span></p>
      <p>Mobile: 0417 862 095<span class="sep">|</span>Email: MD@CoralwoodEstatePartners.com.au</p>
    </div>
    <div class="footer-brand wordmark">Coralwood Estate Partners</div>

    <div class="rule rule--bottom"></div>
    <div class="band band--bottom"></div>
  </section>

  <section class="sheet sheet--back">
    <div class="rule rule--top"></div>
    <div class="cover-brand wordmark">Coralwood<br>Estate Partners</div>
    <div class="rule rule--bottom"></div>
  </section>

  <p class="sheet-label sheet-label--front">Front</p>
  <p class="sheet-label sheet-label--back">Back</p>
</body>
</html>
```